Strata Edge Supply Business Card Design Challenge

Please create me a simple card using my logo. I'm not looking for anything abstract.
A couple of colours for text and maybe something on the card so the whole card isn't just a white board.
Please send me samples and I'll reply with suggestions to refine the design. Thank you

Reason: The Ormeau address was incorrect in the brief, so I have updated that so the 4 and 5 star submissions can be updated and resubmitted please!!! Sorry and thank you

Target Market(s)

Mining companies and rock producing aggregate companies. Quarries

Industry/Entity Type

Mining

Contact Information for Business Card

Name - Lewis Trenholm / Company Logo AND Strata Edge Supply Pty Ltd / position - Managing Director / address1 - Unit 3, 14 Kestrel Parade, Ormeau 4208 Queensland AU / address2 - PO Box 917, Oxenford 4210 Queensland AU / mobile - 0427 195 864 / phone - 07 5571 9346 / fax - 07 5571 9420 / email - lt@strataedgesupply.example.com.au / website - www.strataedgesupply.example.com.au

Requirements
Must have
• Business details as per the above. The phone and fax numbers will be confirmed before the end of the project. Thank you
• SINGLE SIDED ONLY please on Card, not transparent plastic

```html
<!DOCTYPE html>
<html lang="en">
<head>
<meta charset="utf-8">
<title>Strata Edge Supply – Business Card</title>
<link href="https://fonts.googleapis.com/css2?family=Open+Sans:wght@400;600;700&family=Orbitron:wght@600&display=swap" rel="stylesheet">
<style>
  :root {
    --backdrop: #e4e2de;
    --card-white: #ffffff;
    --band-grey: #4a4d51;
    --band-grey-dark: #3d4044;
    --accent-blue: #29a3dc;
    --text-grey: #55585c;
    --rule-grey: #8a8d90;
    --band-text: #ffffff;
  }
  * { box-sizing: border-box; margin: 0; padding: 0; }
  html, body {
    width: 1200px; height: 1023px; overflow: hidden;
    background: var(--backdrop);
    font-family: "Open Sans", Arial, sans-serif;
  }
  .card {
    position: absolute; left: 100px; top: 226px;
    width: 1000px; height: 570px;
    background: var(--card-white);
    box-shadow: 0 6px 24px rgba(0,0,0,.18);
    overflow: hidden;
  }
  .top-rule {
    position: absolute; left: 60px; right: 60px; top: 46px;
    height: 2px; background: var(--rule-grey);
  }
  .identity {
    position: absolute; left: 0; right: 0; top: 92px;
    text-align: center;
  }
  .brand {
    display: inline-flex; align-items: center; gap: 16px;
    font-weight: 700; font-size: 46px; color: var(--text-grey);
    letter-spacing: 1px; line-height: 1.2;
  }
  .brand-square { width: 30px; height: 30px; background: var(--accent-blue); }
  .brand-rule {
    width: 380px; height: 2px; background: var(--rule-grey);
    margin: 22px auto 18px;
  }
  .person-name {
    font-family: "Orbitron", "Open Sans", sans-serif;
    font-weight: 600; font-size: 30px; letter-spacing: 3px;
    color: var(--accent-blue); text-transform: uppercase;
  }
  .person-role { font-size: 22px; color: var(--text-grey); margin-top: 4px; }
  .contact-band {
    position: absolute; left: 0; right: 0; bottom: 0; height: 212px;
    background: linear-gradient(180deg, var(--band-grey), var(--band-grey-dark));
    border-top: 5px solid var(--accent-blue);
    border-bottom: 5px solid var(--accent-blue);
    color: var(--band-text);
    display: flex; justify-content: space-between;
    padding: 22px 48px;
    font-size: 19px; line-height: 33px;
  }
  .contact-list, .address-list { list-style: none; }
  .contact-list li { display: flex; align-items: center; gap: 12px; white-space: nowrap; }
  .address-list { text-align: right; }
  .address-list li { display: flex; align-items: center; justify-content: flex-end; gap: 12px; white-space: nowrap; }
  .company-name { color: var(--accent-blue); font-weight: 400; }
  .icon {
    width: 20px; height: 20px; flex: none;
    background: var(--accent-blue); border-radius: 3px;
    display: inline-flex; align-items: center; justify-content: center;
  }
  .icon svg { width: 14px; height: 14px; fill: #fff; }
  .icon-blank { width: 20px; flex: none; }
</style>
</head>
<body>
<div class="card">
  <div class="top-rule"></div>
  <div class="identity">
    <div class="brand"><span class="brand-square"></span>Strata Edge Supply</div>
    <div class="brand-rule"></div>
    <div class="person-name">Lewis Trenholm</div>
    <div class="person-role">Managing Director</div>
  </div>
  <div class="contact-band">
    <ul class="contact-list">
      <li><span class="icon"><svg viewBox="0 0 16 16"><rect x="4" y="1" width="8" height="14" rx="1.5"/></svg></span>0427 195 864</li>
      <li><span class="icon"><svg viewBox="0 0 16 16"><path d="M3 2l3 0 1 3-2 1.5a8 8 0 0 0 4.5 4.5L11 9l3 1v3a1 1 0 0 1-1 1A12 12 0 0 1 2 3a1 1 0 0 1 1-1z"/></svg></span>07 5571 9346</li>
      <li><span class="icon"><svg viewBox="0 0 16 16"><rect x="2" y="6" width="12" height="7" rx="1"/><rect x="4" y="2" width="8" height="4"/></svg></span>07 5571 9420</li>
      <li><span class="icon"><svg viewBox="0 0 16 16"><path d="M1 4h14v9H1z M1 4l7 5 7-5" stroke="#29a3dc" stroke-width="1"/></svg></span>lt@strataedgesupply.example.com.au</li>
      <li><span class="icon"><svg viewBox="0 0 16 16"><circle cx="8" cy="8" r="6"/></svg></span>www.strataedgesupply.example.com.au</li>
    </ul>
    <ul class="address-list">
      <li class="company-name">Strata Edge Supply Pty Ltd<span class="icon"><svg viewBox="0 0 16 16"><path d="M8 1a5 5 0 0 1 5 5c0 4-5 9-5 9S3 10 3 6a5 5 0 0 1 5-5z"/></svg></span></li>
      <li>Unit 3, 14 Kestrel Parade<span class="icon-blank"></span></li>
      <li>Kestrel Downs 4216 Queensland AU<span class="icon-blank"></span></li>
      <li>PO Box 917 Ridgeford<span class="icon"><svg viewBox="0 0 16 16"><path d="M1 4h14v9H1z"/></svg></span></li>
      <li>4218 Queensland AU<span class="icon-blank"></span></li>
    </ul>
  </div>
</div>
</body>
</html>
```